Colorful Live Music Concert Poster for Tin Harbor

Looking for a portrait oriented "poster" promoting the band's upcoming show at Marlow Lounge on Sunday, 3/22 at 8 pm, and social version (square format for Instagram). <br/><br/>Copy:<br/>Tin Harbor<br/>with The Pale Wires<br/><br/>Marlow Lounge <br/>Sunday, March 22<br/>8 pm<br/><br/>Poster must be consistent with band's overall branding seen on www.tinharborband.example and it's Tunevault page at https://music.example.com/artist/7QxRtaWpLeNmVcz2Ks9DuB?si=381fkTsYpWmaGHeLoRqdXC <br/><br/>BUT, we wouldn't mind taking in a slightly updated direction. A good example is the cover for our recent single Glad Today, which is consistent in theme and color palette while updating the design and color at the same time. <br/><br/>The attached files include some band logo art as well as examples of posters done for prior shows. <br/><br/>The posters need not include photos of the band, but if you are so inclined, we've uploaded some selects as well.<br/><br/>Thank you. <br/><br/>Wendell<br/>Tin Harbor

```html
<!DOCTYPE html>
<html lang="en">
<head>
<meta charset="utf-8">
<title>Tin Harbor — Live at Marlow Lounge</title>
<link rel="stylesheet" href="https://fonts.googleapis.com/css2?family=Lato:wght@400;700&display=swap">
<style>
  :root {
    --navy: #233059;
    --teal: #1fa0a5;
    --sun: #fbb820;
    --sun-deep: #f6a91b;
  }
  * { margin: 0; padding: 0; box-sizing: border-box; }
  html, body { width: 856px; height: 1200px; overflow: hidden; background: var(--navy); }
  .poster {
    position: relative;
    width: 856px;
    height: 1200px;
    overflow: hidden;
    font-family: "Lato", Arial, sans-serif;
    color: var(--navy);
  }
  .backdrop { position: absolute; inset: 0; }
  .band-name {
    position: absolute;
    left: 0; right: 0; top: 52px;
    text-align: center;
    color: var(--sun);
    font-weight: 700;
    text-transform: uppercase;
    line-height: 1;
  }
  .band-name span { display: block; letter-spacing: 0.12em; padding-left: 0.12em; }
  .band-name .line-one { font-size: 156px; }
  .band-name .line-two { font-size: 138px; margin-top: 22px; }
  .show-details {
    position: absolute;
    left: 117px; top: 415px;
    width: 620px; height: 620px;
    display: flex; flex-direction: column; align-items: center; justify-content: center;
    text-align: center;
    text-transform: uppercase;
    line-height: 1;
  }
  .support-small { font-size: 36px; }
  .support-act { font-size: 62px; margin-top: 14px; }
  .venue { font-size: 74px; font-weight: 700; margin-top: 22px; }
  .day { font-size: 36px; margin-top: 30px; }
  .date { font-size: 66px; margin-top: 12px; }
  .time { font-size: 36px; margin-top: 14px; }
  .socials {
    position: absolute;
    left: 0; right: 0; top: 1116px;
    display: flex; justify-content: center; gap: 54px;
    font-size: 19px;
  }
  .social { display: flex; align-items: center; gap: 9px; }
  .social-dot { width: 26px; height: 26px; border-radius: 5px; background: var(--navy); }
</style>
</head>
<body>
<main class="poster">
  <svg class="backdrop" width="856" height="1200" viewBox="0 0 856 1200" aria-hidden="true">
    <rect width="856" height="1200" fill="var(--navy)"/>
    <polygon points="0,849 856,432 856,1200 0,1200" fill="var(--teal)"/>
    <circle cx="427" cy="725" r="331" fill="none" stroke="var(--sun)" stroke-width="6"/>
    <circle cx="427" cy="725" r="310" fill="var(--sun)" role="img" aria-label="Yellow brick wall texture"/>
  </svg>

  <h1 class="band-name">
    <span class="line-one">Tin</span>
    <span class="line-two">Harbor</span>
  </h1>

  <section class="show-details">
    <p class="support-small">The</p>
    <p class="support-act">Pale Wires</p>
    <p class="venue">Marlow Lounge</p>
    <p class="day">Sunday</p>
    <p class="date">March 22</p>
    <p class="time">8:00 PM</p>
  </section>

  <footer class="socials">
    <span class="social"><span class="social-dot"></span>@tinharborband</span>
    <span class="social"><span class="social-dot"></span>@tinharborband</span>
    <span class="social"><span class="social-dot"></span>/tinharborband</span>
  </footer>
</main>
</body>
</html>
```